Stylish Business Card for Modern hair salon

I need a simple business card design using our salon logo and colours that are in the logo. We service clients of all ages but predominantly those in the 18 to 55 age range. We have a young staff and are looking to have a card that will present a modern and clean image that represents who we are. The card should be in black and white same as our logo. Minimal use of other colours is allowed.

Industry/Entity Type

Hair And Beauty

Contact Information for Business Card

The design should have the following information
salon name - TZ Hair Studio
address - 2957 Fernbrook Rd.W. Mississauga, ON L8R3P2
phone - 905 641-2087
website - tzhairexample.ca
instagram - tz.hairstudio
twitter - @TZ_HairStudio

Colors
000000
ffffff
474747

Requirements
Must have
• simple design, salon name, address, phone, website, instagram, twitter info
• Back of card should have the following:
• YOUR NEXT APPOINTMENT
• DATE
• TIME
Nice to have
• simple design, clear to see and read,
• predominantly black and white colour, minimal use of other colours is ok
Should not have
• many colours, various fonts

```html
<!DOCTYPE html>
<html lang="en">
<head>
<meta charset="utf-8">
<title>TZ Hair Studio – Business Card</title>
<link rel="stylesheet" href="https://fonts.googleapis.com/css2?family=Roboto:wght@400;500&family=Roboto+Condensed:wght@400&display=swap">
<style>
  :root {
    --black: #000000;
    --white: #ffffff;
    --grey: #474747;
    --paper: #f4f4f4;
    --name-grey: #b5b5b5;
    --backdrop: #e6e3df;
  }
  * { box-sizing: border-box; margin: 0; padding: 0; }
  html, body {
    width: 1200px; height: 960px; overflow: hidden;
    background: var(--backdrop);
    font-family: "Roboto", Arial, sans-serif;
  }
  .card {
    position: absolute;
    width: 601px; height: 343px;
  }
  .card--front { left: 314px; top: 113px; background: var(--black); color: var(--white); }
  .card--back { left: 311px; top: 472px; background: var(--paper); color: var(--black); }

  .brand-name {
    position: absolute; right: 34px;
    font-family: "Roboto", Arial, sans-serif;
    font-weight: 500; font-size: 30px; letter-spacing: 3px;
    text-transform: uppercase; white-space: nowrap;
  }
  .card--front .brand-name { top: 92px; color: var(--white); }
  .card--back .brand-name { top: 72px; right: 60px; color: var(--black); }

  .person { position: absolute; left: 34px; top: 182px; }
  .person__name {
    font-family: "Roboto Condensed", Arial, sans-serif;
    font-size: 23px; color: var(--name-grey); text-transform: uppercase; line-height: 1;
  }
  .person__title { font-size: 15px; font-weight: 500; margin-top: 8px; letter-spacing: .3px; }

  .divider {
    position: absolute; left: 34px; right: 34px; top: 241px;
    border-top: 1px solid #8a8a8a;
  }

  .contacts { position: absolute; left: 34px; top: 256px; list-style: none; font-size: 14px; }
  .contacts li { display: flex; align-items: center; height: 19px; }
  .contacts svg { width: 12px; height: 12px; margin-right: 11px; fill: #d0d0d0; }

  .address {
    position: absolute; right: 34px; top: 256px;
    font-size: 14px; text-align: right; font-style: normal;
  }
  .address span { display: block; height: 19px; line-height: 19px; }
  .address .web { letter-spacing: 1.4px; }

  .appointment { position: absolute; left: 57px; right: 60px; top: 200px; }
  .appointment__title { font-size: 19px; font-weight: 500; margin-bottom: 17px; }
  .field-row { display: flex; align-items: baseline; font-size: 16px; height: 43px; }
  .field-row .leader {
    flex: 1; border-bottom: 1px dotted var(--grey); margin: 0 3px 0 4px; transform: translateY(-3px);
  }
  .field-row .leader--date { flex: 0 0 222px; }
  .field-row .ampm { font-size: 12px; margin-left: 2px; }
</style>
</head>
<body>

<section class="card card--front">
  <div class="brand-name">TZ Hair Studio</div>

  <div class="person">
    <div class="person__name">Daniel Reyes</div>
    <div class="person__title">CEO/FOUNDER</div>
  </div>

  <div class="divider"></div>

  <ul class="contacts">
    <li>
      <svg viewBox="0 0 24 24" aria-hidden="true"><path d="M6.6 10.8a15.1 15.1 0 0 0 6.6 6.6l2.2-2.2c.3-.3.7-.4 1-.2 1.1.4 2.3.6 3.6.6.6 0 1 .4 1 1V20c0 .6-.4 1-1 1A17 17 0 0 1 3 4c0-.6.4-1 1-1h3.5c.6 0 1 .4 1 1 0 1.3.2 2.5.6 3.6.1.3 0 .7-.2 1z"/></svg>
      905 641-2087
    </li>
    <li>
      <svg viewBox="0 0 24 24" aria-hidden="true"><circle cx="12" cy="12" r="8"/></svg>
      @TZ_HairStudio
    </li>
    <li>
      <svg viewBox="0 0 24 24" aria-hidden="true"><rect x="4" y="4" width="16" height="16"/></svg>
      tz.hairstudio
    </li>
  </ul>

  <address class="address">
    <span>2957 Fernbrook Rd.W</span>
    <span>Mississauga, ON L8R3P2</span>
    <span class="web">www.tzhairexample.ca</span>
  </address>
</section>

<section class="card card--back">
  <div class="brand-name">TZ Hair Studio</div>

  <div class="appointment">
    <div class="appointment__title">Your Next Appointment</div>
    <div class="field-row"><span>Name:</span><span class="leader"></span></div>
    <div class="field-row">
      <span>Date:</span><span class="leader leader--date"></span>
      <span>Time:</span><span class="leader"></span><span class="ampm">AM/PM</span>
    </div>
  </div>
</section>

</body>
</html>
```